Valdrimo

We need logo and wesbsite for a software development company based out of Hyderabad, India focused on startups and mid sized companies focused on build a new software products in USA and Europe countires.

Target Market(s)

startup and midsized companies in teh USA and Europe for software product development.

Industry/Entity Type

software development

Coding

Coded - Design and coding required

Number of Pages Required

5+ page

Requirements
Must have
• latest design concepts and very elegant
Nice to have
• each page should have images that reflects the content
Should not have
• too many colors

```html
<!DOCTYPE html>
<html lang="en">
<head>
<meta charset="utf-8">
<title>Valdrimo — Software Development</title>
<link href="https://fonts.googleapis.com/css2?family=Audiowide&family=Lato:wght@400;700;900&display=swap" rel="stylesheet">
<style>
:root{
  --green:#14806a;
  --green-dark:#0d5e4e;
  --orange:#ef5a24;
  --ink:#222;
  --text:#555;
  --dark:#1c1c1c;
  --white:#fff;
  --line:#e2e2e2;
}
*{margin:0;padding:0;box-sizing:border-box}
html,body{width:1200px;height:4389px;overflow:hidden}
body{position:relative;background:var(--white);font-family:'Lato',sans-serif;color:var(--text)}
.abs{position:absolute}
.display{font-family:'Audiowide',sans-serif;color:var(--ink);font-weight:400}
.btn{position:absolute;display:flex;align-items:center;justify-content:center;background:var(--orange);color:var(--white);font:700 14px 'Lato',sans-serif;letter-spacing:.3px;border-bottom:3px solid #c9441a}
/* header */
.site-header{position:absolute;left:0;top:0;width:1200px;height:100px;background:var(--white)}
.brand{position:absolute;left:145px;top:26px;display:flex;align-items:center;gap:14px;font:900 38px 'Lato',sans-serif;color:var(--ink);letter-spacing:.5px}
.brand-mark{width:34px;height:34px;background:var(--green)}
.nav{position:absolute;top:38px;left:528px;display:flex;gap:28px;font:700 14px 'Lato',sans-serif;color:var(--ink)}
.nav .active{border-bottom:3px solid var(--green);padding-bottom:6px}
/* hero */
.hero-photo{position:absolute;left:0;top:100px;width:1200px;height:612px;background:linear-gradient(120deg,#6c7680 0%,#2d3238 45%,#15181c 100%);clip-path:polygon(0 0,100% 0,100% 77%,0 100%)}
.hero-card{position:absolute;left:77px;top:218px;width:491px;height:353px;background:rgba(20,128,106,.93)}
.hero-title{position:absolute;left:138px;top:228px;font-size:52px;line-height:66px;color:var(--white)}
.hero-sub{position:absolute;left:140px;top:382px;width:400px;font:700 15px/23px 'Lato',sans-serif;color:var(--white)}
.slider-dots{position:absolute;left:147px;top:628px;display:flex;gap:7px;align-items:center}
.slider-dots .dot{width:6px;height:6px;border-radius:50%;background:var(--white)}
.slider-dots .on{background:var(--green)}
/* about */
.about-device{position:absolute;left:68px;top:724px;width:409px;height:452px;background:linear-gradient(160deg,#f4f4f4,#dcdcdc);border-radius:18px}
.section-title{position:absolute;font-size:50px;line-height:60px}
.about-text{position:absolute;left:542px;top:840px;width:513px;font-size:13.5px;line-height:27px;text-align:justify}
/* product */
.product-title{left:0;width:1200px;text-align:center;top:1360px;color:var(--white)}
.center-text{position:absolute;left:200px;width:800px;text-align:center;color:var(--white)}
.role-grid{position:absolute;left:143px;top:1701px;display:flex;gap:10px}
.role{width:174px;height:143px;border:1.5px solid rgba(255,255,255,.85);display:flex;flex-direction:column;align-items:center;justify-content:flex-end;padding-bottom:22px;color:var(--white);font:700 14px 'Lato',sans-serif}
.role svg{margin-bottom:20px}
/* team */
.team-title{left:0;width:1200px;text-align:center;top:2201px}
.team-text{position:absolute;left:250px;width:700px;text-align:center;font-size:13.5px;line-height:27px}
.step-title{position:absolute;width:260px;text-align:center;font:400 19px/23px 'Lato',sans-serif;color:var(--ink)}
.step-text{position:absolute;width:240px;font-size:13px;line-height:22.5px;text-align:justify;text-align-last:center}
/* case */
.case-title{left:143px;top:3195px;color:var(--white)}
.case-text{position:absolute;left:143px;top:3286px;width:491px;font-size:14px;line-height:27.3px;color:#e8e8e8;text-align:justify}
.case-photo{position:absolute;left:718px;top:3176px;width:419px;height:426px;background:linear-gradient(135deg,#8b7a68 0%,#3b4148 55%,#1e2226 100%)}
/* contact */
.contact-title{left:0;width:1200px;text-align:center;top:3861px}
.contact{position:absolute;top:3999px;width:260px;text-align:center}
.contact .ring{width:72px;height:72px;margin:0 auto;border-radius:50%;border:2px solid #999;display:flex;align-items:center;justify-content:center}
.contact .ring.solid{background:var(--green);border-color:var(--green)}
.contact h4{margin-top:24px;font:700 15px 'Lato',sans-serif;color:var(--ink)}
.contact p{margin-top:10px;font-size:13px;line-height:22px}
.footer-rule{position:absolute;left:0;top:4214px;width:1200px;height:1px;background:var(--line)}
.copyright{position:absolute;top:4251px;left:0;width:1200px;text-align:center;font-size:12.5px}
.social{position:absolute;top:4309px;left:482px;display:flex;gap:14px}
.social span{width:48px;height:48px;border-radius:50%;border:2px solid var(--ink);display:flex;align-items:center;justify-content:center}
.social span.solid{background:var(--ink)}
</style>
</head>
<body>

<header class="site-header">
  <div class="brand"><span class="brand-mark"></span>VALDRIMO</div>
  <nav class="nav">
    <span class="active">ABOUT US</span><span>BUILD YOUR PRODUCT</span><span>BUILD YOUR TEAM</span><span>CASE STUDY</span>
  </nav>
</header>

<section>
  <div class="hero-photo" role="img" aria-label="Photo of hands typing code on a laptop at a desk"></div>
  <div class="hero-card"></div>
  <h1 class="display hero-title">Software<br>Development</h1>
  <p class="hero-sub">Lorem ipsum dolor sit amet, consectetur adipiscing elit, sed do eiusmod tempor incididunt ut labore</p>
  <div class="btn" style="left:140px;top:464px;width:172px;height:36px">REQUEST A DEMO</div>
  <div class="slider-dots">
    <svg width="18" height="18" viewBox="0 0 18 18"><circle cx="9" cy="9" r="8" fill="#fff"/><path d="M10.5 5.5L7 9l3.5 3.5" fill="none" stroke="#333" stroke-width="1.6"/></svg>
    <span class="dot on"></span><span class="dot"></span><span class="dot"></span><span class="dot"></span><span class="dot"></span>
    <svg width="18" height="18" viewBox="0 0 18 18"><circle cx="9" cy="9" r="8" fill="#fff"/><path d="M7.5 5.5L11 9l-3.5 3.5" fill="none" stroke="#333" stroke-width="1.6"/></svg>
  </div>
  <svg class="abs" style="left:588px;top:620px" width="24" height="14" viewBox="0 0 24 14"><path d="M2 2l10 9 10-9" fill="none" stroke="#bbb" stroke-width="2"/></svg>
</section>

<section>
  <div class="about-device" role="img" aria-label="Illustration of a desktop monitor showing a search web page"></div>
  <h2 class="display section-title" style="left:540px;top:759px">About Us</h2>
  <p class="about-text">Teams are the essence of every business. They can create wonders if built with perfection.We are a group of entrepreneurs, technocrats, software architects, and delivery heads who have come together to serve startups, product companies, and enterprises with their product development. We are prompt in understanding your product and help design, build, maintain and operate your product. Valdrimo quickly set up a team of UX experts, Business Analysts, Developers and QA resources to build the best team to deliver the product.</p>
  <div class="btn" style="left:542px;top:1060px;width:171px;height:40px">READ MORE</div>
</section>

<section>
  <svg class="abs" style="left:0;top:0" width="1200" height="4389" role="img" aria-label="Green tinted photo of a laptop with code on screen">
    <defs><linearGradient id="pg" x1="0" y1="0" x2="1" y2="1"><stop offset="0" stop-color="#1a8f77"/><stop offset="1" stop-color="#0e6a58"/></linearGradient></defs>
    <polygon points="29,1321 1171,1108 1171,2194 29,1943" fill="url(#pg)"/>
  </svg>
  <h2 class="display section-title product-title" style="position:absolute">Build Your Product</h2>
  <p class="center-text" style="top:1455px;font-size:17px;line-height:27.5px">As startups are racing to build software as a product, they have stumbling blocks on building software from scratch. One of the reasons is stiff competition.The competition to get the best resources, robust design, and scalable technology is overwhelming.</p>
  <p class="center-text" style="top:1558px;font-size:14px;line-height:27px">Startup owners must use the CEO mindset while building a software product. Think of the bigger picture. Focus on the outcome and set aside the tiny technical details. Focus on human resources and Process.</p>
  <p class="center-text" style="top:1619px;font-size:15.5px;font-weight:700">Software development needs experts. Thus, your team will include:</p>
  <div class="role-grid">
    <div class="role">
      <svg width="60" height="60" viewBox="0 0 60 60" fill="none" stroke="#fff" stroke-width="2.2"><rect x="14" y="10" width="32" height="42" rx="3"/><rect x="23" y="6" width="14" height="8" rx="2"/><path d="M20 26l4 4 7-7M34 27h8M20 40l4 4 7-7M34 41h8"/></svg>
      PROJECT MANAGER</div>
    <div class="role">
      <svg width="60" height="60" viewBox="0 0 60 60" fill="none" stroke="#fff" stroke-width="2.2"><path d="M30 8l22 11-22 11L8 19z"/><path d="M8 30l22 11 22-11M8 41l22 11 22-11"/></svg>
      TEAM LEAD</div>
    <div class="role">
      <svg width="60" height="60" viewBox="0 0 60 60" fill="none" stroke="#fff" stroke-width="2.2"><rect x="8" y="8" width="44" height="44" rx="3"/><path d="M18 42V32M26 42V22M34 42V28M42 42V16"/></svg>
      BUSINESS ANALYST</div>
    <div class="role">
      <svg width="60" height="60" viewBox="0 0 60 60" fill="none" stroke="#fff" stroke-width="2.2"><rect x="6" y="10" width="48" height="34" rx="3"/><path d="M22 50h16M30 44v6M24 21l-7 6 7 6M36 21l7 6-7 6M32 19l-4 16"/></svg>
      DEVELOPERS</div>
    <div class="role">
      <svg width="60" height="60" viewBox="0 0 60 60" fill="none" stroke="#fff" stroke-width="2.2"><circle cx="30" cy="30" r="22"/><path d="M20 30l7 7 14-14"/></svg>
      TESTERS</div>
  </div>
  <div class="btn" style="left:515px;top:1895px;width:170px;height:38px">READ MORE</div>
</section>

<section>
  <h2 class="display section-title team-title" style="position:absolute">Build Your Team</h2>
  <p class="team-text" style="top:2298px">Break free from traditional recruiting with us. At Valdrimo, we help you achieve the right organizational matrix with rockstars who can take your business to the next level.</p>
  <p class="team-text" style="top:2359px">We have spent years trying to innovate and improve the process of hiring talented individuals who can take businesses to the next level. We ensure that the workforce we employ for your organization is highly productive and takes you to the golden standards of heights.</p>

  <svg class="abs" style="left:0;top:2480px" width="1200" height="170" viewBox="0 2480 1200 170">
    <g font-family="Audiowide, sans-serif" font-size="110" fill="none" stroke="#222" stroke-width="2.5">
      <text x="140" y="2610">1</text><text x="498" y="2610">2</text><text x="868" y="2610">3</text>
    </g>
    <g fill="none" stroke="#222" stroke-width="2">
      <circle cx="247" cy="2565" r="53"/><circle cx="612" cy="2565" r="53"/><circle cx="992" cy="2565" r="53"/>
    </g>
    <circle cx="247" cy="2565" r="43" fill="var(--green)"/>
    <rect x="228" y="2548" width="38" height="26" rx="2" fill="none" stroke="#fff" stroke-width="4"/>
    <path d="M240 2584h14M247 2574v10" stroke="#fff" stroke-width="4"/>
    <path d="M596 2582l4-12 22-22 8 8-22 22z" fill="var(--green)"/>
    <circle cx="986" cy="2565" r="19" fill="var(--green)"/>
    <g fill="none" stroke="#fff" stroke-width="2"><ellipse cx="986" cy="2565" rx="8" ry="19"/><path d="M967 2565h38M970 2555h32M970 2575h32"/></g>
    <path d="M315 2535q90-45 180 10" fill="none" stroke="#888" stroke-width="1.5" stroke-dasharray="3 4"/>
    <path d="M488 2537l8 10-12 2" fill="#888"/>
    <path d="M688 2590q90 55 180 0" fill="none" stroke="#888" stroke-width="1.5" stroke-dasharray="3 4"/>
    <path d="M860 2584l12 4-8 9" fill="#888"/>
  </svg>

  <h3 class="step-title" style="left:107px;top:2657px">Pass cognitive<br>aptitude test</h3>
  <h3 class="step-title" style="left:474px;top:2652px">Pass English<br>Proficiency test</h3>
  <h3 class="step-title" style="left:825px;top:2652px">Prove real-world<br>job skills</h3>
  <p class="step-text" style="left:117px;top:2720px">Accepting job applications from the entire world means every role on Valdrimo receives thousands of applications. We find that the</p>
  <p class="step-text" style="left:473px;top:2720px">Someday, technological advancements will make it possible for teams to collaborate without sharing a common language. Until then, English</p>
  <p class="step-text" style="left:837px;top:2720px">Of course, there's much more to being a great worker than intelligence and language skills. The next step is to complete a real-world job</p>
  <div class="btn" style="left:152px;top:2840px;width:172px;height:38px">READ MORE</div>
  <div class="btn" style="left:505px;top:2840px;width:172px;height:38px">READ MORE</div>
  <div class="btn" style="left:871px;top:2840px;width:172px;height:38px">READ MORE</div>
</section>

<section>
  <svg class="abs" style="left:0;top:0" width="1200" height="4389">
    <polygon points="29,3136 1171,2954 1171,3866 29,3682" fill="var(--dark)"/>
    <rect x="897" y="3366" width="274" height="277" fill="var(--green)"/>
  </svg>
  <h2 class="display section-title case-title" style="position:absolute">Case Study</h2>
  <p class="case-text">Many business owners have great ideas but no experience with the actual product. Once you have an idea in mind, you will require software development aid at some point – whether your concept is for next-generation software or an inventive approach to offering an existing service. It might also be the development of a mobile app or web-based software. Whatever product you're working on, you'll need a technical co-founder to help you get it off the ground. An MVP can help you turn your vision into reality.</p>
  <div class="btn" style="left:143px;top:3537px;width:172px;height:38px">READ MORE</div>
  <div class="case-photo" role="img" aria-label="Photo of two developers working together at a computer screen"></div>
</section>

<section>
  <h2 class="display section-title contact-title" style="position:absolute">Get In Touch</h2>
  <div class="contact" style="left:86px">
    <div class="ring"><svg width="26" height="26" viewBox="0 0 24 24"><path d="M6.6 10.8a15 15 0 006.6 6.6l2.2-2.2a1 1 0 011-.25 11.4 11.4 0 003.6.6 1 1 0 011 1V20a1 1 0 01-1 1A17 17 0 013 4a1 1 0 011-1h3.5a1 1 0 011 1c0 1.25.2 2.45.6 3.6a1 1 0 01-.25 1z" fill="var(--green)"/></svg></div>
    <h4>PHONE</h4><p>(+1) 555 014 2290</p>
  </div>
  <div class="contact" style="left:311px">
    <div class="ring"><svg width="22" height="28" viewBox="0 0 24 30"><path d="M12 1a10 10 0 00-10 10c0 7.5 10 18 10 18s10-10.5 10-18A10 10 0 0012 1z" fill="var(--green)"/><circle cx="12" cy="11" r="4" fill="#fff"/></svg></div>
    <h4>HEAD OFFICE</h4><p>27 Marlow Quay Lane, Old Harbor,<br>Westbury, USA. PO 5173</p>
  </div>
  <div class="contact" style="left:591px">
    <div class="ring solid"><svg width="22" height="28" viewBox="0 0 24 30"><path d="M12 1a10 10 0 00-10 10c0 7.5 10 18 10 18s10-10.5 10-18A10 10 0 0012 1z" fill="#fff"/><circle cx="12" cy="11" r="4" fill="var(--green)"/></svg></div>
    <h4>MAIN OFFICE</h4><p>27 Marlow Quay Lane, Old Harbor,<br>Westbury, USA. PO 5173</p>
  </div>
  <div class="contact" style="left:840px">
    <div class="ring"><svg width="28" height="20" viewBox="0 0 28 20"><rect width="28" height="20" rx="2" fill="var(--green)"/><path d="M1 2l13 9 13-9" fill="none" stroke="#fff" stroke-width="2"/></svg></div>
    <h4>EMAIL</h4><p>info@valdrimo.com</p>
  </div>
</section>

<footer>
  <div class="footer-rule"></div>
  <p class="copyright">Copyrights © 2022, Valdrimo.All rights reserved &nbsp;|&nbsp; Privacy policy &nbsp;|&nbsp; Site Map &nbsp;|&nbsp; Disclaimer &nbsp;|&nbsp; Terms of use</p>
  <div class="social" aria-label="Social links">
    <span aria-label="Share"><svg width="20" height="20" viewBox="0 0 20 20" fill="none" stroke="#222" stroke-width="2"><path d="M5 15L15 5M8 5h7v7"/></svg></span>
    <span aria-label="Link"><svg width="20" height="20" viewBox="0 0 20 20" fill="none" stroke="#222" stroke-width="2"><path d="M8 12l4-4M7 9l-2 2a3 3 0 004 4l2-2M13 11l2-2a3 3 0 00-4-4l-2 2"/></svg></span>
    <span class="solid" aria-label="Plus"><svg width="20" height="20" viewBox="0 0 20 20" fill="none" stroke="#fff" stroke-width="2.4"><path d="M10 4v12M4 10h12"/></svg></span>
    <span aria-label="Play"><svg width="20" height="20" viewBox="0 0 20 20"><path d="M7 5l8 5-8 5z" fill="#222"/></svg></span>
  </div>
</footer>

</body>
</html>
```